VB Heating & Cooling / 2018 Brenk Moviro Medium Roof / 148"wb

Customer is looking for a new design on his new 2018 brenk moviro medium roof 148"wb van. This will be a Full Wrap.

Attached is: >Customers logo
> Template for the van he has (You don't have to use this exact one for the proof)

Please include: > Slogan- Quality work at reasonable prices
>(555) 019-4821
>Services- Repairs, installation, maintenance, water heaters, indoor air quality
>Residential & Commercial

```html
<!DOCTYPE html>
<html lang="en">
<head>
<meta charset="utf-8">
<title>VB Heating &amp; Cooling – Van Wrap</title>
<link rel="stylesheet" href="https://fonts.googleapis.com/css2?family=Barlow+Condensed:ital,wght@0,600;0,700;1,600&family=Montserrat:wght@600;700&display=swap">
<style>
  :root {
    --orange: #ea7a1f;
    --orange-deep: #d9661a;
    --orange-light: #f29a3a;
    --navy: #2b3e9c;
    --red: #c4202b;
    --cream: #e9e9ea;
    --white: #ffffff;
    --ink: #111111;
    --logo-blue: #2f72c0;
    --page: #ffffff;
  }
  html, body {
    margin: 0;
    width: 960px;
    height: 1200px;
    overflow: hidden;
    background: var(--page);
  }
  .canvas {
    position: relative;
    width: 960px;
    height: 1200px;
  }
  .wrap-side, .wrap-rear { position: absolute; display: block; }
  .wrap-side { left: 0; top: 60px; width: 960px; height: 340px; }
  .wrap-rear { left: 190px; top: 450px; width: 580px; height: 690px; }

  .headline {
    font-family: "Barlow Condensed", sans-serif;
    font-weight: 600;
    text-anchor: middle;
  }
  .headline--side { fill: var(--navy); font-size: 30px; }
  .headline--rear { fill: var(--red); font-size: 42px; }

  .brand-name {
    font-family: "Barlow Condensed", sans-serif;
    font-weight: 700;
    fill: var(--logo-blue);
    text-anchor: middle;
  }
  .brand-name--side { font-size: 32px; }
  .brand-name--rear { font-size: 48px; }

  .service {
    font-family: "Montserrat", sans-serif;
    font-weight: 600;
    font-size: 15px;
    fill: var(--white);
  }
  .slogan {
    font-family: "Barlow Condensed", sans-serif;
    font-weight: 600;
    font-style: italic;
    fill: var(--ink);
    stroke: var(--white);
    stroke-width: 3px;
    paint-order: stroke;
  }
  .slogan--side { font-size: 36px; }
  .slogan--rear { font-size: 42px; font-style: normal; text-anchor: middle; }

  .phone {
    font-family: "Montserrat", sans-serif;
    font-weight: 700;
    paint-order: stroke;
  }
  .phone--side { font-size: 28px; fill: var(--red); stroke: var(--white); stroke-width: 3px; }
  .phone--rear { font-size: 56px; fill: #fbe3e4; stroke: var(--red); stroke-width: 5px; text-anchor: middle; }

  .web-address {
    font-family: "Barlow Condensed", sans-serif;
    font-weight: 600;
    font-size: 24px;
    fill: var(--white);
    text-anchor: middle;
  }
</style>
</head>
<body>
<main class="canvas">

  <!-- Side panel -->
  <svg class="wrap-side" viewBox="0 0 960 340" aria-label="Van side wrap">
    <defs>
      <linearGradient id="flameSide" x1="0" y1="0" x2="0" y2="1">
        <stop offset="0" stop-color="var(--orange-light)"/>
        <stop offset="1" stop-color="var(--orange-deep)"/>
      </linearGradient>
      <clipPath id="sidePanel"><rect x="40" y="10" width="880" height="300" rx="24"/></clipPath>
    </defs>
    <g clip-path="url(#sidePanel)">
      <rect class="flame-field" x="40" y="10" width="880" height="300" fill="url(#flameSide)" role="img" aria-label="Orange flame pattern background"/>
      <path class="services-field" d="M40,10 H250 C262,60 280,120 300,165 C316,200 338,222 370,232 H40 Z" fill="var(--navy)"/>
      <ellipse class="badge-ring" cx="420" cy="0" rx="200" ry="250" fill="var(--red)"/>
      <ellipse class="badge-face" cx="420" cy="0" rx="178" ry="226" fill="var(--cream)"/>
    </g>

    <text class="headline headline--side" x="420" y="56">Residential &amp; Commercial</text>
    <text class="brand-name brand-name--side" x="420" y="132">VB Heating &amp; Cooling</text>

    <g class="services-list">
      <text class="service" x="82" y="62">•Repairs</text>
      <text class="service" x="82" y="88">•Installation</text>
      <text class="service" x="82" y="114">•Maintenance</text>
      <text class="service" x="82" y="140">•Water Heaters</text>
      <text class="service" x="82" y="166">•Indoor Air Quality</text>
    </g>

    <text class="slogan slogan--side" x="74" y="272">Quality work at reasonable prices</text>
    <text class="phone phone--side" x="620" y="270">(555) 019-4821</text>
  </svg>

  <!-- Rear panel -->
  <svg class="wrap-rear" viewBox="0 0 580 690" aria-label="Van rear wrap">
    <defs>
      <linearGradient id="flameRear" x1="0" y1="0" x2="0" y2="1">
        <stop offset="0" stop-color="var(--orange-light)"/>
        <stop offset="1" stop-color="var(--orange-deep)"/>
      </linearGradient>
      <clipPath id="rearPanel"><rect x="0" y="0" width="580" height="690" rx="30"/></clipPath>
    </defs>
    <g clip-path="url(#rearPanel)">
      <rect class="flame-field" x="0" y="0" width="580" height="690" fill="url(#flameRear)" role="img" aria-label="Orange flame pattern background"/>
      <ellipse class="badge-ring" cx="290" cy="0" rx="272" ry="475" fill="var(--red)"/>
      <ellipse class="badge-face" cx="290" cy="0" rx="242" ry="442" fill="var(--cream)"/>
      <rect class="contact-band" x="0" y="560" width="580" height="130" fill="var(--navy)"/>
    </g>

    <text class="headline headline--rear" x="290" y="94">Residential &amp; Commercial</text>
    <text class="brand-name brand-name--rear" x="290" y="230">VB Heating &amp; Cooling</text>
    <text class="slogan slogan--rear" x="290" y="535">Quality work at reasonable prices</text>
    <text class="phone phone--rear" x="290" y="636">(555) 019-4821</text>
    <text class="web-address" x="290" y="674">vbheatcoolservice.com</text>
  </svg>

</main>
</body>
</html>
```